Stationary Package for New Bookkeeping Business

We need the following stationary designs:

- Business Card
- Letterhead
- With Comps
- Envelopes
- Paper Folder
- Email Signature

We will provide accounting and bookkeeping services to small business. We would like have the main color as blue and have a modern professional look.

Variations of colour and shades of blue welcome
Preference for deeper darker blue - navy

Variations of font in logo also welcome

Requirements
Must have
• Rosalind
B.Bus (Accounting)
Registered BAS Agent

Phone 0491 382 507
Post PO Box 947 Kelmora NSW 2768

Email rosalind@tarwinledgers.com

Business Card to be bold and eye catching

Should not have
• Letter head to not have too much colour on it

```html
<!DOCTYPE html>
<html lang="en">
<head>
<meta charset="utf-8">
<title>Tarwin Ledgers – Email Signature</title>
<link rel="stylesheet" href="https://fonts.googleapis.com/css2?family=Arimo:wght@400&display=swap">
<style>
  :root {
    --paper: #ffffff;
    --ink: #2e2e2e;
    --navy: #2b3650;
    --muted-navy: #3a4660;
  }
  html, body {
    margin: 0;
    padding: 0;
    width: 1200px;
    height: 900px;
    overflow: hidden;
    background: var(--paper);
  }
  .canvas {
    position: relative;
    width: 1200px;
    height: 900px;
    font-family: "Arimo", Arial, sans-serif;
    color: var(--ink);
  }
  .signature {
    position: absolute;
    left: 300px;
    top: 170px;
  }
  .sig-name {
    margin: 0;
    font-size: 52px;
    font-weight: 400;
    line-height: 1.1;
    letter-spacing: -0.5px;
  }
  .sig-title {
    margin: 4px 0 0;
    font-size: 37px;
    line-height: 1.2;
    text-transform: uppercase;
  }
  .sig-contact {
    margin: 38px 0 0;
    font-size: 36px;
    line-height: 1.2;
  }
  .sig-contact .label {
    display: inline-block;
    width: 40px;
  }
  .sig-post {
    margin: 36px 0 0;
    font-size: 36px;
    line-height: 1.2;
  }
  .brand {
    display: flex;
    align-items: center;
    gap: 18px;
    margin-top: 34px;
  }
  .brand-square {
    width: 64px;
    height: 64px;
    background: var(--navy);
  }
  .brand-name {
    font-size: 60px;
    line-height: 1;
    color: var(--navy);
  }
  .sig-web {
    margin: 18px 0 0;
    font-size: 36px;
    color: var(--muted-navy);
  }
</style>
</head>
<body>
  <div class="canvas">
    <div class="signature">
      <p class="sig-name">Rosalind B.Bus (Accounting)</p>
      <p class="sig-title">Registered BAS Agent</p>
      <p class="sig-contact"><span class="label">T</span>0491 382 507<br><span class="label">E</span>rosalind@tarwinledgers.com</p>
      <p class="sig-post">Post PO Box 947<br>Kelmora NSW 2768</p>
      <div class="brand">
        <div class="brand-square"></div>
        <div class="brand-name">Tarwin Ledgers</div>
      </div>
      <p class="sig-web">www.tarwinledgers.com</p>
    </div>
  </div>
</body>
</html>
```